3D Brochure
Brochure
Project: 3D Brochure
3D Brochure - Environment
Creative Brief
Environment
Corporate, Industrial
Trifold brochure. Must include some "Bleed" for printing.

```html
<!DOCTYPE html>
<html lang="en">
<head>
<meta charset="utf-8">
<title>Harbor Crest Environmental – Trifold Brochure</title>
<link href="https://fonts.googleapis.com/css2?family=Open+Sans:wght@400;600;700;800&display=swap" rel="stylesheet">
<style>
:root{
  --bg:#e9e9e9;
  --panel-top:#3a3d42;
  --panel-bottom:#121315;
  --bar-top:#5b6068;
  --bar-bottom:#25282c;
  --text:#e8ecf0;
  --muted:#aab3bd;
  --accent:#c3161c;
  --photo-a:#6f7680;
  --photo-b:#cfd4d8;
}
*{box-sizing:border-box;margin:0;padding:0}
html,body{width:1200px;height:926px;overflow:hidden;background:var(--bg);font-family:"Open Sans",Arial,sans-serif;color:var(--text)}
.stage{position:relative;width:1200px;height:926px;display:flex;gap:20px;align-items:center;justify-content:center}
.spread{width:580px;height:448px;display:flex;box-shadow:0 4px 16px rgba(0,0,0,.35)}
.panel{flex:1;min-width:0;padding:10px 9px;background:linear-gradient(180deg,var(--panel-top),var(--panel-bottom));border-right:1px solid #000;display:flex;flex-direction:column;gap:6px;position:relative;overflow:hidden}
.panel:last-child{border-right:none}
.bar{background:linear-gradient(180deg,var(--bar-top),var(--bar-bottom));border-radius:6px;padding:3px 8px;font-size:8.5px;font-weight:700;text-transform:uppercase;letter-spacing:.3px;border:1px solid #6c727a}
.copy{font-size:6.6px;line-height:1.45;color:var(--text)}
.copy.muted{color:var(--muted)}
.list{list-style:none;font-size:6.6px;line-height:1.5}
.list li::before{content:"\25B8";color:var(--muted);margin-right:4px}
.contacts{display:grid;grid-template-columns:1fr auto;font-size:6.6px;line-height:1.6}
.photo{background:linear-gradient(135deg,var(--photo-b),var(--photo-a));border-radius:4px;border:1px solid #777}
.row{display:flex;gap:6px}
.row .photo{flex:1}
.office{font-size:6.6px;line-height:1.5;text-align:center}
.office strong{font-weight:700;font-size:7px}
.cover{align-items:center;justify-content:flex-start;background:linear-gradient(180deg,#2a2d31,#0d0e10)}
.brand{margin-top:40px;display:flex;align-items:center;gap:6px}
.brand-square{width:14px;height:14px;flex:none;background:var(--muted)}
.brand-name{font-size:11px;font-weight:700;text-transform:uppercase;letter-spacing:.4px}
.response{margin-top:auto;text-align:center;font-weight:800;font-size:10px;line-height:1.3}
.badge{width:34px;height:34px;border-radius:50%;background:var(--accent);margin:6px auto 4px}
</style>
</head>
<body>
<main class="stage">

  <section class="spread outside" aria-label="Outside of trifold">
    <div class="panel">
      <div class="bar">Environmental Services</div>
      <p class="copy">We maintain a large inventory of equipment, trucks and trained crews ready to serve the region around the clock. Call us for your needs.</p>
    </div>
    <div class="panel">
      <div class="bar">Certificates &amp; Qualifications</div>
      <ul class="list">
        <li>OSHA Trained</li>
        <li>Hazwoper Certified</li>
        <li>Confined Space Entry</li>
        <li>First Aid / CPR Trained</li>
        <li>Licensed Waste Hauler</li>
        <li>Certified Tank Remover</li>
        <li>Certified Site Assessor</li>
        <li>Fully Insured</li>
      </ul>
      <div class="bar">Emergency Contacts</div>
      <div class="contacts">
        <span>Rowan Pike</span><span>555-201-3381</span>
        <span>Ellis Moreno</span><span>555-201-3372</span>
        <span>Dana Whitlow</span><span>555-201-3390</span>
      </div>
      <div class="bar">Office</div>
      <div class="office">
        <strong>Harbor Crest Environmental, LLC</strong><br>
        418-C Quarry Bend Rd<br>
        Millbrook, ST 00417<br><br>
        Phone: 555-014-7700<br>
        Fax: 555-014-7711<br>
        office@harborcrestenv.example
      </div>
    </div>
    <div class="panel cover">
      <div class="brand">
        <span class="brand-square"></span>
        <span class="brand-name">Harbor Crest Environmental, LLC</span>
      </div>
      <div class="row" style="width:100%;height:56px;margin-top:30px">
        <div class="photo" role="img" aria-label="Vacuum truck on site"></div>
        <div class="photo" role="img" aria-label="Tanker truck in yard"></div>
      </div>
      <div class="photo" role="img" aria-label="Crew with cleanup equipment" style="width:100%;height:52px"></div>
      <div class="response">24 HOUR RESPONSE<br>555-014-7700</div>
      <div class="badge" aria-hidden="true"></div>
    </div>
  </section>

  <section class="spread inside" aria-label="Inside of trifold">
    <div class="panel">
      <div class="bar">Air, Soil &amp; Spill Cleanup</div>
      <div class="photo" role="img" aria-label="Spill response truck" style="height:58px"></div>
      <p class="copy">Specialized response equipment and trained personnel ready for any spill or release, large or small.</p>
      <ul class="list">
        <li>Traffic Crashes</li>
        <li>Containment Booms</li>
        <li>Roll-off Containers</li>
        <li>Spill Prevention Plans</li>
        <li>Removal of Storage Tanks</li>
      </ul>
      <p class="copy muted">Licensed personnel and all of the necessary equipment to handle removals of any size.</p>
      <ul class="list">
        <li>Soil Testing &amp; Sampling</li>
        <li>Monitoring Well Installs</li>
      </ul>
    </div>
    <div class="panel">
      <div class="bar">Vacuum Truck Services</div>
      <div class="row" style="height:50px">
        <div class="photo" role="img" aria-label="Vacuum truck working"></div>
        <p class="copy" style="flex:1">Grit and sludge removal, oil recovery and wash water pickup.</p>
      </div>
      <div class="bar">Tank Cleaning</div>
      <div class="row" style="height:50px">
        <p class="copy" style="flex:1">Fuel, chemical and process tanks cleaned by our trained crews.</p>
        <div class="photo" role="img" aria-label="Tank cleaning crew"></div>
      </div>
      <div class="photo" role="img" aria-label="Large pipe section on ground" style="height:60px"></div>
      <p class="copy">The vacuum system provides the most complete removal of waste and solids, with full disposal records kept.</p>
    </div>
    <div class="panel">
      <div class="bar">Remediation &amp; Reclamation</div>
      <div class="photo" role="img" aria-label="Shoreline remediation work" style="height:60px"></div>
      <p class="copy">Rapid response to any release on water or land, with trained crews and equipment always standing by.</p>
      <ul class="list">
        <li>High Pressure Water Blasting</li>
      </ul>
      <div class="bar">Liquid Transport</div>
      <p class="copy">We have 100,000 gallons of liquid storage available.</p>
      <ul class="list">
        <li>Disposal of Liquids / Sludge</li>
        <li>Soil Disposal / Remediation</li>
        <li>Used Oil Recycling</li>
        <li>Non-Haz Drum Removal</li>
        <li>Lab Pack Disposal</li>
      </ul>
    </div>
  </section>

</main>
</body>
</html>
```